Tervolan Pty Ltd professional business card

A professional business card template using the colours from the supplied logo.
Clean crisp lines while, Modern while not being over the top.

Target Market(s)

Construction, commerical and industrial

Industry/Entity Type

Communications

Contact Information for Business Card

For a Communications, IT, Optical fibre installation company

Colors
37b8a4

```html
<!DOCTYPE html>
<html lang="en">
<head>
<meta charset="utf-8">
<title>Tervolan Pty Ltd – Business Card</title>
<link href="https://fonts.googleapis.com/css2?family=Roboto:wght@300;400;500&display=swap" rel="stylesheet">
<style>
  :root {
    --backdrop: #e9e9e9;
    --card: #2d2d2e;
    --teal: #2b9ba6;
    --white: #ffffff;
    --soft: #d9d9d9;
    --rule: #cfcfcf;
  }
  * { margin: 0; padding: 0; box-sizing: border-box; }
  html, body { width: 1200px; height: 801px; overflow: hidden; }
  body {
    background: var(--backdrop);
    font-family: "Roboto", Arial, sans-serif;
    position: relative;
  }
  .card {
    position: absolute;
    width: 500px;
    height: 286px;
    background: var(--card);
    border-bottom: 4px solid var(--teal);
    box-shadow: 0 10px 24px rgba(0,0,0,.18);
    overflow: hidden;
  }
  .card--front { left: 70px; top: 258px; }
  .card--back  { left: 630px; top: 258px; }

  .brand {
    position: absolute;
    display: flex;
    align-items: center;
    gap: 10px;
    color: var(--white);
    font-weight: 500;
    letter-spacing: 2px;
  }
  .brand__dot {
    width: 16px; height: 16px;
    border-radius: 50%;
    background: var(--teal);
  }
  .card--front .brand { right: 40px; top: 58px; font-size: 38px; }
  .card--back .brand  { right: 40px; top: 120px; font-size: 40px; }

  .divider {
    position: absolute;
    left: 40px; right: 34px; top: 140px;
    height: 1.5px;
    background: var(--rule);
  }
  .person {
    position: absolute;
    left: 40px; bottom: 150px;
  }
  .person__name { color: var(--teal); font-size: 21px; font-weight: 500; }
  .person__role { color: var(--soft); font-size: 15px; font-weight: 300; margin-top: 1px; }

  .contact {
    position: absolute;
    left: 40px; top: 156px;
    list-style: none;
    color: var(--soft);
    font-size: 14.5px;
    font-weight: 300;
  }
  .contact li { display: flex; align-items: center; gap: 10px; line-height: 24px; }
  .contact svg { width: 12px; height: 12px; flex: none; }
  .contact .accent { color: var(--teal); }

  .address {
    position: absolute;
    right: 40px; top: 156px;
    text-align: right;
    color: var(--soft);
    font-size: 14.5px;
    font-weight: 300;
    line-height: 20px;
  }
</style>
</head>
<body>

<section class="card card--front" aria-label="Business card front">
  <div class="brand"><span class="brand__dot"></span>TERVOLAN</div>
  <div class="person">
    <p class="person__name">Daniel Harrow</p>
    <p class="person__role">Manager</p>
  </div>
  <div class="divider"></div>
  <ul class="contact">
    <li>
      <svg viewBox="0 0 12 12" aria-hidden="true"><path d="M2.5 1 4.5 3.2 3.4 4.6c.8 1.6 2.1 2.9 3.7 3.7L8.5 7.2 11 9.2 9.8 11C5.2 10.6 1.4 6.8 1 2.2Z" fill="var(--teal)"/></svg>
      123-456-2100
    </li>
    <li>
      <svg viewBox="0 0 12 12" aria-hidden="true"><rect x="1" y="2.5" width="10" height="7" rx="1" fill="none" stroke="var(--teal)" stroke-width="1.2"/><path d="M1.5 3 6 6.6 10.5 3" fill="none" stroke="var(--teal)" stroke-width="1.2"/></svg>
      youremail@mailbox.com
    </li>
    <li>
      <svg viewBox="0 0 12 12" aria-hidden="true"><circle cx="6" cy="6" r="5" fill="none" stroke="var(--teal)" stroke-width="1.2"/><path d="M1 6h10M6 1c-2.4 2.8-2.4 7.2 0 10M6 1c2.4 2.8 2.4 7.2 0 10" fill="none" stroke="var(--teal)" stroke-width="1"/></svg>
      <span>www.<span class="accent">yourwebsite</span>.com</span>
    </li>
  </ul>
  <p class="address">Your address, city<br>state, ZIP 0000</p>
</section>

<section class="card card--back" aria-label="Business card back">
  <div class="brand"><span class="brand__dot"></span>TERVOLAN</div>
</section>

</body>
</html>
```